Real Estate agent needs flyer/folder to contain bio and overview of services

I'm including files of the layout of the small folder. The folder is 6 1/2 across and 9 1/2 inches long. It will have a front & back cover and then writing on the 2 inside pages.

I am sending a few files to incorporate into the flyer, 1 new logo to use and 2 files which are coloring ideas.

```html
<!DOCTYPE html>
<html lang="en">
<head>
<meta charset="utf-8">
<title>Marlowe Homes Folder</title>
<link rel="stylesheet" href="https://fonts.googleapis.com/css2?family=Open+Sans:ital,wght@0,400;0,600;0,700;1,400&display=swap">
<style>
:root{
  --navy:#14213a;
  --navy-deep:#0b1426;
  --navy-soft:#243a5e;
  --red:#c8232c;
  --blue:#1f6fb5;
  --sky:#5fa7df;
  --ink:#3a3f47;
  --silver:#d9dde4;
  --paper:#ffffff;
}
*{margin:0;padding:0;box-sizing:border-box}
html,body{width:900px;height:1200px;overflow:hidden;background:#fff}
body{font-family:"Open Sans",Arial,sans-serif;color:var(--ink)}
.folder{position:relative;width:900px;height:1200px}
.cover{position:absolute;top:0;width:450px;height:595px;
  background:radial-gradient(ellipse at 40% 30%,var(--navy-soft) 0%,var(--navy) 45%,var(--navy-deep) 100%)}
.cover-back{left:0}
.cover-front{left:450px;border-left:1px solid #0a1120}
.tagline{position:absolute;left:50px;right:40px;top:178px;color:var(--silver);
  font-size:11px;font-style:italic;line-height:1.5;text-align:center}
.partner-mark{position:absolute;left:0;right:0;top:270px;display:flex;align-items:center;justify-content:center;gap:10px}
.partner-mark .dot{width:44px;height:44px;border-radius:50%;background:var(--red)}
.partner-mark .name{color:#fff;font-weight:700;font-size:20px}
.contact{position:absolute;left:0;right:0;top:378px;text-align:center;color:var(--silver);font-size:11px;line-height:1.6}
.contact .agent{color:#fff;font-weight:700;font-size:14px}
.brand{position:absolute;left:0;right:0;top:225px;display:flex;flex-direction:column;align-items:center;gap:14px}
.brand .ring{width:120px;height:120px;border-radius:50%;border:3px solid var(--silver)}
.brand .name{color:#fff;font-weight:700;font-size:30px;letter-spacing:1px}
.page{position:absolute;top:600px;width:450px;height:600px;background:var(--paper)}
.page-left{left:0;padding:30px 34px 20px 38px}
.page-right{left:450px;border-left:1px solid #e3e6ea}
h2{color:var(--red);font-size:11.5px;font-weight:700;margin:10px 0 4px}
p{font-size:9px;line-height:1.55;margin-bottom:6px}
.page-left p{font-size:9.6px;line-height:1.7;margin-bottom:7px}
.page-left h2{margin-top:12px}
.waves{position:absolute;left:0;top:0;width:450px;height:280px}
.portrait{position:absolute;left:30px;top:18px;width:175px;height:215px;border-radius:4px;
  background:linear-gradient(160deg,#e9d3b8 0%,#c9a77e 45%,#3d4a63 100%)}
.intro{position:absolute;left:224px;right:22px;top:28px}
.intro h2{margin-top:0}
.team{position:absolute;left:30px;right:28px;top:282px}
.closing{font-size:13px;line-height:1.5;color:var(--ink);margin-top:8px}
</style>
</head>
<body>
<div class="folder">
  <section class="cover cover-back">
    <p class="tagline">Selling and buying your home, I'm a lifelong resource for all things house-related &amp; beyond... if you need a great referral for anything at all call me! I can't wait to work with you!</p>
    <div class="partner-mark"><span class="dot"></span><span class="name">Summit Realty</span></div>
    <div class="contact">
      <div class="agent">Dana Marlowe</div>
      <div>555-014-2290</div>
      <div>dana@marlowehomes.example</div>
      <div>www.marlowehomes.example</div>
    </div>
  </section>

  <section class="cover cover-front">
    <div class="brand"><span class="ring"></span><span class="name">Marlowe Homes</span></div>
  </section>

  <section class="page page-left">
    <h2>Selling your Home</h2>
    <p>Selling your home is not the same as buying one. As your agent I will guide each step, from pricing and staging to marketing and closing, so your property reaches the right buyers quickly.</p>
    <p>I use proven online tools, print campaigns and my network of local agents to create strong interest. Every showing is followed up and you receive clear weekly updates on progress.</p>
    <p>When an offer arrives I review every term with you, negotiate firmly on your behalf and coordinate inspections, appraisals and paperwork until the keys change hands.</p>
    <p>Before listing, I prepare a detailed market report so your price is grounded in recent local sales, and I suggest simple updates that help your home stand out.</p>
    <h2>Buying a home</h2>
    <p>Buying a home is one of the biggest decisions you will make. I listen to your needs, budget and timeline, then search listings daily so you see the best options first.</p>
    <p>I arrange viewings, share honest advice on value and condition, and connect you with trusted lenders and inspectors. From first visit to final signature I stay by your side.</p>
    <p>If you are relocating, I can tour homes for you by video, explain neighborhoods, schools and commute times, and keep your move on schedule from afar.</p>
    <h2>In summary</h2>
    <p>Whether you are selling, buying or simply exploring the market, you deserve an agent who is responsive, knowledgeable and committed to your goals. Call me today and let us start planning your next move together.</p>
    <p>Many of my clients come back to me years later or send their friends and family my way, and that trust is the reward I value most in this work.</p>
  </section>

  <section class="page page-right">
    <svg class="waves" viewBox="0 0 450 280" aria-hidden="true">
      <path d="M0 0 H235 C215 70 150 130 0 160 Z" fill="#14213a"/>
      <path d="M0 205 C70 245 150 255 215 222 V236 C150 272 70 262 0 224 Z" fill="#1f6fb5"/>
      <path d="M0 236 C80 274 160 278 215 248 V258 C160 290 80 284 0 250 Z" fill="#5fa7df"/>
    </svg>
    <div class="portrait" role="img" aria-label="Portrait photo of the agent"></div>
    <div class="intro">
      <h2>Let me introduce myself</h2>
      <p>I am a licensed agent with more than fifteen years of experience in the local market. I grew up here, raised my family here and know every neighborhood by heart.</p>
      <p>My passion is helping people find homes they love and guiding sellers to the best possible outcome.</p>
    </div>
    <div class="team">
      <h2>My Core Team</h2>
      <p>My team includes a transaction coordinator, a marketing specialist and a trusted network of lenders, inspectors and contractors ready to help.</p>
      <h2>Real Estate Services &amp; Beyond</h2>
      <p>From first time buyers to seasoned investors, I offer pricing guidance, staging advice, relocation help and referrals for anything your home may need.</p>
      <p class="closing">I also provide a team who is dedicated to providing outstanding customer service throughout the transaction. My team includes a network of lenders, title partners, in house VPs, stagers, photographers, contractors and more.</p>
    </div>
  </section>
</div>
</body>
</html>
```